TOP NOTCH CATALOG RE-DESIGN FOR A NATIONAL BRAND

This Project needs to be redesigned with a new look and feel we will use all the same tires and keep the same writing we will only change the model numbers from QZ to DW then the number
please visit www.dravelonwheels.example for feel of site which will direct your imagination

Target Market(s)

Our Target Market is Truck Drivers throughout the USA

Industry/Entity Type

Trucking Company

Font styles to use
Serif

Requirements
Must have
• Yellow and Black this signify our Brand see attached Logo
Nice to have
• Lion since our logo is that shows a strong product
Should not have
• other tires other than what is listed

```html
<!DOCTYPE html>
<html lang="en">
<head>
<meta charset="utf-8">
<title>Dravelon Wheels Catalog Cover</title>
<link rel="stylesheet" href="https://fonts.googleapis.com/css2?family=Roboto+Slab:wght@300;700;900&family=Roboto+Serif:wght@400;500&display=swap">
<style>
  :root {
    --backdrop: #9a9a9a;
    --paper: #f7f7f7;
    --ink: #111111;
    --muted: #666666;
    --title-grey: #8a8a8a;
    --orange: #e8621a;
    --yellow: #e3b20d;
    --yellow-light: #f4cf63;
    --navy: #22214a;
    --steel: #7d7f8c;
    --white: #ffffff;
  }
  * { margin: 0; padding: 0; box-sizing: border-box; }
  html, body {
    width: 1200px; height: 804px; overflow: hidden;
    background: var(--backdrop);
  }
  .cover {
    position: absolute; left: 330px; top: 20px;
    width: 540px; height: 764px;
    background: var(--paper);
    overflow: hidden;
    box-shadow: 0 6px 18px rgba(0,0,0,0.25);
    font-family: "Roboto Serif", Georgia, serif;
  }
  .cover-art { position: absolute; inset: 0; width: 540px; height: 764px; }
  .intro-note {
    position: absolute; left: 34px; top: 76px; width: 200px;
    font-size: 7.5px; line-height: 1.35; color: var(--ink);
  }
  .brand {
    position: absolute; right: 34px; top: 60px;
    display: flex; align-items: center; gap: 8px;
  }
  .brand-dot { width: 14px; height: 14px; border-radius: 50%; background: var(--ink); }
  .brand-name {
    font-family: "Roboto Slab", Georgia, serif;
    font-size: 16px; font-weight: 900; color: var(--ink);
    letter-spacing: 0.3px; text-transform: uppercase;
  }
  .title {
    position: absolute; left: 0; right: 0; top: 150px;
    text-align: center; font-size: 44px; line-height: 1;
    font-family: "Roboto Slab", Georgia, serif;
  }
  .title-strong { color: var(--orange); font-weight: 700; }
  .title-light { color: var(--title-grey); font-weight: 300; }
  .mission {
    position: absolute; left: 105px; right: 105px; top: 210px;
    text-align: center; font-size: 8.5px; line-height: 1.45; color: var(--muted);
  }
  .site-url {
    position: absolute; right: 40px; top: 688px;
    font-size: 15px; letter-spacing: 1px; color: var(--white); font-weight: 400;
  }
</style>
</head>
<body>
  <main class="cover">
    <svg class="cover-art" viewBox="0 0 540 764" xmlns="http://www.w3.org/2000/svg">
      <defs>
        <radialGradient id="wheel-photo-tone" cx="0.55" cy="0.45" r="0.65">
          <stop offset="0" stop-color="#a9abb5"/>
          <stop offset="0.45" stop-color="#7d7f8c"/>
          <stop offset="1" stop-color="#22214a"/>
        </radialGradient>
      </defs>
      <polygon class="accent-band-light" points="0,322 160,262 540,282 540,296 160,276 0,336" fill="#f4cf63"/>
      <polygon class="accent-band" points="0,336 160,276 540,296 540,304 165,286 0,346" fill="#e3b20d"/>
      <polygon class="wheel-photo" role="img" aria-label="Photo of four truck tires on alloy wheels lined up on a dark studio floor"
               points="0,346 165,286 540,304 540,470 270,570 0,560" fill="url(#wheel-photo-tone)"/>
      <polygon class="stripe-orange" points="0,560 270,570 540,470 540,484 275,586 0,576" fill="#e8621a"/>
      <polygon class="stripe-white" points="0,576 275,586 540,484 540,500 280,606 0,592" fill="#ffffff"/>
      <polygon class="base-yellow" points="0,592 280,606 540,500 540,764 0,764" fill="#e3b20d"/>
      <polygon class="stripe-yellow-light" points="0,592 280,606 540,500 540,506 282,614 0,600" fill="#f4cf63"/>
    </svg>

    <p class="intro-note">At Dravelon Wheels, we always want to ensure that the tires are always compatible with your vehicle needs.</p>

    <div class="brand">
      <span class="brand-dot"></span>
      <span class="brand-name">Dravelon Wheels</span>
    </div>

    <h1 class="title"><span class="title-strong">Dravelon</span> <span class="title-light">Wheels</span></h1>

    <p class="mission">At Dravelon Wheels our mission is to earn and develop long lasting relationships with our customers and business partners, through responsive actions, a dedication to quality and the highest standard of manufacturing.</p>

    <p class="site-url">www.dravelonwheels.example</p>
  </main>
</body>
</html>
```